LA Billboard Project for Brisk Lending

We are running three different billboards around LA, and we need someone to take the mock-ups I've created and bring this campaign to life. Whatever wording is on the mock-ups should stay the same in the ads you create, but feel free to get creative with layout and style. I've attached our mock-ups, our style guide, our logo, and the necessary specs for the billboards. If you have any questions, feel free to reach out!

```html
<!DOCTYPE html>
<html lang="en">
<head>
<meta charset="UTF-8">
<title>Brisk Lending – Billboard</title>
<link rel="stylesheet" href="https://fonts.googleapis.com/css2?family=Montserrat:wght@300;400;600;700&display=swap">
<style>
  :root {
    --stage: #262626;
    --navy: #1d2c5d;
    --teal: #4cc3dc;
    --yellow: #ffe000;
    --white: #ffffff;
    --ink: #16234d;
  }
  * { margin: 0; padding: 0; box-sizing: border-box; }
  html, body {
    width: 720px;
    height: 1200px;
    overflow: hidden;
    background: var(--stage);
    font-family: "Montserrat", Arial, sans-serif;
  }
  .billboard {
    position: absolute;
    left: 20px;
    top: 443px;
    width: 680px;
    height: 314px;
    background: var(--navy);
    overflow: hidden;
    box-shadow: 0 14px 30px rgba(0,0,0,0.55);
  }
  .billboard__art {
    position: absolute;
    inset: 0;
    width: 680px;
    height: 314px;
  }
  .brand {
    position: absolute;
    left: 39px;
    top: 34px;
    display: flex;
    align-items: center;
    gap: 8px;
    color: var(--teal);
    font-weight: 700;
    font-size: 27px;
    letter-spacing: -0.3px;
  }
  .brand__square {
    width: 14px;
    height: 14px;
    background: var(--teal);
  }
  .headline {
    position: absolute;
    left: 39px;
    top: 114px;
    height: 100px;
    padding-left: 13px;
    border-left: 2px solid var(--yellow);
    text-transform: uppercase;
    line-height: 1;
  }
  .headline__lead {
    display: block;
    color: var(--white);
    font-weight: 300;
    font-size: 25px;
    margin-bottom: 8px;
  }
  .headline__accent {
    display: block;
    color: var(--yellow);
    font-weight: 700;
    font-size: 29px;
    margin-bottom: 8px;
  }
  .headline__close {
    display: block;
    color: var(--teal);
    font-weight: 700;
    font-size: 29px;
  }
  .web-link {
    position: absolute;
    left: 40px;
    top: 258px;
    display: flex;
    align-items: center;
    gap: 9px;
    color: var(--ink);
    font-weight: 600;
    font-size: 22px;
  }
  .web-link svg { width: 22px; height: 22px; }
</style>
</head>
<body>
  <section class="billboard" aria-label="Brisk Lending billboard">
    <svg class="billboard__art" viewBox="0 0 680 314" aria-hidden="true">
      <defs>
        <linearGradient id="photoTones" x1="0" y1="0" x2="0" y2="1">
          <stop offset="0" stop-color="#3c4064"/>
          <stop offset="0.18" stop-color="#a87686"/>
          <stop offset="0.32" stop-color="#767078"/>
          <stop offset="0.52" stop-color="#5e5048"/>
          <stop offset="0.66" stop-color="#3f4a3a"/>
          <stop offset="0.78" stop-color="#2d2f35"/>
          <stop offset="1" stop-color="#3a3b41"/>
        </linearGradient>
      </defs>
      <polygon class="web-band" points="0,248 268,248 282,291 0,291" fill="#ffe000"/>
      <path class="arc arc--teal" d="M345 0 Q240 157 352 314 L680 314 L680 0 Z" fill="#4cc3dc"/>
      <path class="arc arc--yellow" d="M352 0 Q258 157 372 314 L680 314 L680 0 Z" fill="#ffe000"/>
    </svg>
    <svg class="billboard__art" viewBox="0 0 680 314" role="img" aria-label="Photo of modern townhouses along a quiet street at dusk">
      <path d="M360 0 Q276 157 378 314 L680 314 L680 0 Z" fill="url(#photoTones)"/>
    </svg>

    <div class="brand"><span class="brand__square"></span>Brisk Lending</div>

    <h1 class="headline">
      <span class="headline__lead">What's your</span>
      <span class="headline__accent">Mortgage</span>
      <span class="headline__close">Strategy?</span>
    </h1>

    <div class="web-link">
      <svg viewBox="0 0 24 24" aria-hidden="true">
        <circle cx="12" cy="12" r="10" fill="none" stroke="#16234d" stroke-width="2"/>
        <ellipse cx="12" cy="12" rx="4.5" ry="10" fill="none" stroke="#16234d" stroke-width="1.6"/>
        <line x1="2" y1="12" x2="22" y2="12" stroke="#16234d" stroke-width="1.6"/>
        <line x1="4" y1="7" x2="20" y2="7" stroke="#16234d" stroke-width="1.4"/>
        <line x1="4" y1="17" x2="20" y2="17" stroke="#16234d" stroke-width="1.4"/>
      </svg>
      brisklending.com
    </div>
  </section>
</body>
</html>
```